Amber Reed Properties, which offers a selection of prime properties (villas

A website that contains: Idea, benefits, destinations (villas), offers, about us, contact, newsletter, social media, blog, look at the attachment, even if it is in German. The idea is that I can easily add new pages, if necessary, with the design you make. Later on we want to add a reservation system, so you can book your villa through the internet. Besides, there is a concierge service available, which organizes everything for the customer, owner, from villa to restaurant, limo service, ... & benefits and emotions through nice pictures / videos, they should be convinced to invest.

Target Market(s)

Investors (golfer and non-golfer) which have 300'000 to invest in a kind of real-estate investing club

Number of Pages Required

5+ page

Font styles to use
Sans Serif

Requirements
Must have
• It must be for wordpress, must have an exclusive touch, high quality, with nice pictures of golf courses. The Logo is gold so it has to match with gold, the font is segan or segoe semilight or similar, sans serif
Nice to have
• may be as well as the possibility to include videos of the different destinations and houses

```html
<!DOCTYPE html>
<html lang="de">
<head>
<meta charset="utf-8">
<title>Amber Reed Properties – Real Estate Portfolio</title>
<link rel="stylesheet" href="https://fonts.googleapis.com/css2?family=Oswald:wght@300;400&family=Open+Sans:wght@300;400&display=swap">
<style>
  :root{
    --gold:#d4a535;
    --ink:#2b2b2b;
    --dark:#151515;
    --dark-2:#1a1a1a;
    --text:#c4c4c4;
    --rule-light:#8a8a8a;
    --white:#ffffff;
  }
  *{margin:0;padding:0;box-sizing:border-box}
  html,body{width:1200px;height:1200px;overflow:hidden;background:var(--dark)}
  body{position:relative;font-family:"Open Sans",sans-serif;font-weight:300;color:var(--text)}

  .rule{position:absolute;left:547px;width:106px}
  .rule span{display:block;height:1px;margin-bottom:3px}

  .portfolio{position:absolute;left:0;top:0;width:1200px;height:421px;background:var(--gold);overflow:hidden}
  .portfolio__title{position:absolute;top:12px;width:100%;text-align:center;font-family:"Oswald",sans-serif;font-weight:300;font-size:36px;line-height:48px;letter-spacing:.5px;color:var(--ink)}
  .portfolio .rule{top:70px}
  .portfolio .rule span{background:var(--ink)}

  .card{position:absolute;top:96px;width:287px;height:294px;background:var(--white)}
  .card__photo{position:absolute;left:5px;top:5px;right:5px;height:237px}
  .card__label{position:absolute;left:0;right:0;top:250px;height:44px;padding:0 14px;display:flex;align-items:center;justify-content:space-between;font-family:"Oswald",sans-serif;font-weight:300;font-size:17.5px;color:#3a3a3a;white-space:nowrap}
  .card__more{width:29px;height:29px;flex:none}
  .photo-villa-pool{background:linear-gradient(180deg,#6d8fd0 0%,#e6e0e4 45%,#8c6a55 70%,#2a63b8 100%)}
  .photo-golf-resort{background:linear-gradient(180deg,#b9c9c2 0%,#7ea24c 40%,#d6cfa8 60%,#4a4a40 78%,#1d3f78 100%)}
  .photo-golf-lake{background:linear-gradient(180deg,#d5dde8 0%,#d9c9ad 28%,#5f8d35 45%,#8b9aa8 70%,#6c8f3a 100%)}
  .photo-terrace{background:linear-gradient(180deg,#8a9fb4 0%,#b8c3c9 35%,#6f9a4a 60%,#5c4a3a 100%)}

  .benefit{position:absolute;left:0;width:1200px}
  .benefit--monetary{top:421px;height:521px;background:var(--dark);border-bottom:1px solid #222}
  .benefit--practical{top:942px;height:258px;background:var(--dark-2)}
  .benefit .rule span{background:var(--rule-light)}
  .benefit__kicker{position:absolute;width:100%;text-align:center;font-family:"Oswald",sans-serif;font-weight:300;font-size:15px;line-height:20px;color:var(--white);letter-spacing:.3px}
  .benefit__title{position:absolute;width:100%;text-align:center;font-family:"Oswald",sans-serif;font-weight:300;font-size:36px;line-height:42px;color:var(--gold);letter-spacing:1px}
  .benefit__photo{position:absolute;border-radius:5px}
  .benefit__text{position:absolute}
  .benefit__text p{font-size:17px;line-height:21.5px;margin-bottom:13px}
  .benefit__list{list-style:none;margin:4px 0 12px}
  .benefit__list li{font-size:13.3px;line-height:24.7px;padding-left:16px;position:relative}
  .benefit__list li::before{content:"";position:absolute;left:0;top:8.5px;width:9px;height:9px;border-radius:50%;background:#9a9a9a}
  .photo-resort-lake{background:linear-gradient(180deg,#c9d3e4 0%,#d8c8ad 22%,#56802f 42%,#8d9ca9 62%,#6c8a4a 88%,#88b040 100%)}
  .photo-villa-dusk{background:linear-gradient(180deg,#4d7fc8 0%,#9fb4d8 35%,#2a2a2a 60%,#a66a38 100%)}
</style>
</head>
<body>

<section class="portfolio">
  <h1 class="portfolio__title">REAL ESTATE PORTFOLIO</h1>
  <div class="rule"><span></span><span></span></div>

  <article class="card" style="left:-145px">
    <div class="card__photo photo-villa-pool" role="img" aria-label="Photo of a modern white villa with pool and lawn"></div>
    <div class="card__label"><span style="margin-left:auto;margin-right:auto;padding-left:120px">SUM</span>
      <svg class="card__more" viewBox="0 0 30 30"><circle cx="15" cy="15" r="13.5" fill="none" stroke="#2b2b2b" stroke-width="2"/><circle cx="9.5" cy="15" r="2" fill="#2b2b2b"/><circle cx="15" cy="15" r="2" fill="#2b2b2b"/><circle cx="20.5" cy="15" r="2" fill="#2b2b2b"/></svg></div>
  </article>

  <article class="card" style="left:156px">
    <div class="card__photo photo-villa-pool" role="img" aria-label="Photo of a modern villa at dusk with lit pool"></div>
    <div class="card__label"><span>MOREM IIPUSM SUN</span>
      <svg class="card__more" viewBox="0 0 30 30"><circle cx="15" cy="15" r="13.5" fill="none" stroke="#2b2b2b" stroke-width="2"/><circle cx="9.5" cy="15" r="2" fill="#2b2b2b"/><circle cx="15" cy="15" r="2" fill="#2b2b2b"/><circle cx="20.5" cy="15" r="2" fill="#2b2b2b"/></svg></div>
  </article>

  <article class="card" style="left:459px">
    <div class="card__photo photo-golf-resort" role="img" aria-label="Aerial photo of a golf resort with palms, bunkers and fountain lake"></div>
    <div class="card__label"><span>LOREM IPUSM SUM</span>
      <svg class="card__more" viewBox="0 0 30 30"><circle cx="15" cy="15" r="13.5" fill="none" stroke="#2b2b2b" stroke-width="2"/><circle cx="9.5" cy="15" r="2" fill="#2b2b2b"/><circle cx="15" cy="15" r="2" fill="#2b2b2b"/><circle cx="20.5" cy="15" r="2" fill="#2b2b2b"/></svg></div>
  </article>

  <article class="card" style="left:761px">
    <div class="card__photo photo-golf-lake" role="img" aria-label="Photo of resort villas above a golf green and lake"></div>
    <div class="card__label"><span>MOREM PIPS USPFE</span>
      <svg class="card__more" viewBox="0 0 30 30"><circle cx="15" cy="15" r="13.5" fill="none" stroke="#2b2b2b" stroke-width="2"/><circle cx="9.5" cy="15" r="2" fill="#2b2b2b"/><circle cx="15" cy="15" r="2" fill="#2b2b2b"/><circle cx="20.5" cy="15" r="2" fill="#2b2b2b"/></svg></div>
  </article>

  <article class="card" style="left:1060px">
    <div class="card__photo photo-terrace" role="img" aria-label="Photo of a terrace lounge overlooking a golf course and mountains"></div>
    <div class="card__label"><span>REAL ESTATE IPSUM</span></div>
  </article>
</section>

<section class="benefit benefit--monetary">
  <div class="rule" style="top:32px"><span></span><span></span></div>
  <div class="benefit__kicker" style="top:44px">YOUR BENEFIT</div>
  <h2 class="benefit__title" style="top:62px">MONETARY</h2>
  <div class="rule" style="top:106px"><span></span><span></span></div>

  <div class="benefit__photo photo-resort-lake" style="left:129px;top:147px;width:367px;height:342px" role="img" aria-label="Photo of resort villas behind a golf green and lake"></div>

  <div class="benefit__text" style="left:531px;top:143px;width:520px">
    <p>Sie sind Mitbesitzer von exklusiven Immobilien in Topresorts, in wunderschöner, gepflegter und sicherer Umgebung</p>
    <p>Miteigentum ermöglicht Ihnen, Ihre Ferien an verschiedenen Destinationen zu verbringen – Abwechslung ist garantiert</p>
    <p style="margin-bottom:4px">Sie geniessen:</p>
    <ul class="benefit__list">
      <li>Die Privatsphäre in ihren Traumvillen, weltweit, mit Familie und Freunden</li>
      <li>das Spiel auf Top-Golfplätzen und dem Zugang zu privaten Anlagen</li>
      <li>den Besuch der Sehenswürdigkeiten</li>
      <li>Kulinarische Highlights in Insider-Restaurants</li>
      <li>Aufregendes Nightlife in den angesagtesten Clubs</li>
    </ul>
    <p>Sie fördern die nachhaltige Nutzung von Immobilien</p>
    <p>Sie erhalten eine unbezahlbare «Erlebnisrendite»</p>
  </div>
</section>

<section class="benefit benefit--practical">
  <div class="rule" style="top:28px"><span></span><span></span></div>
  <div class="benefit__kicker" style="top:39px">IHR NUTZEN</div>
  <h2 class="benefit__title" style="top:56px">PRAKTISCH</h2>
  <div class="rule" style="top:99px"><span></span><span></span></div>

  <div class="benefit__text" style="left:131px;top:142px;width:540px">
    <p>Sie besitzen Immobilien, ohne sich um den Kauf, Verwaltung und den Unterhalt kümmern zu müssen</p>
    <p>Das Verhältnis von 4 Investoren auf 1 Immobilie garantiert eine sehr gute Verfügbarkeit</p>
    <p>Im Gegensatz zu Badeferien, kann das ganze Jahr über Golf gespielt werden</p>
  </div>

  <div class="benefit__photo photo-villa-dusk" style="left:718px;top:136px;width:351px;height:200px" role="img" aria-label="Photo of a modern villa with balconies at dusk"></div>
</section>

</body>
</html>
```